Flyer Design Project

We want to design a flyer for a laundromat in San Francisco. It will be used to market the services of the laundromat. I am uploading a .jpg file with details to be highlighted. The flyer should be of size 8.5 in x 11 in and should be attractive and hard hitting. The attachment should only be used for the copy, not for design.

Target Market(s)

Laundromat and laundry users

Requirements
Must have
• Must have a attention grabbing headline
Nice to have
• Pictures

```html
<!DOCTYPE html>
<html lang="en">
<head>
<meta charset="utf-8">
<title>Harlow Laundromat Flyer</title>
<link href="https://fonts.googleapis.com/css2?family=Roboto:wght@400;700;900&family=Roboto+Condensed:wght@700&display=swap" rel="stylesheet">
<style>
:root{
  --stage:#151515;
  --navy:#1b3f8c;
  --blue:#2357b0;
  --sky:#3f9fe0;
  --ice:#dff0fb;
  --lime:#a6d13a;
  --ink:#1a1a1a;
  --white:#ffffff;
}
*{margin:0;padding:0;box-sizing:border-box}
html,body{width:1200px;height:900px;overflow:hidden;background:var(--stage)}
body{position:relative;font-family:"Roboto",Arial,sans-serif;color:var(--ink)}
.side-label{position:absolute;top:38px;font-family:"Roboto Condensed",Arial,sans-serif;font-weight:700;font-size:44px;color:var(--white);letter-spacing:1px}
.side-label.front{left:232px}
.side-label.back{left:848px}
.page{position:absolute;top:98px;width:570px;height:747px;overflow:hidden;background:var(--white)}
.page.front{left:20px}
.page.back{left:606px}
.page svg.shapes{position:absolute;inset:0;width:100%;height:100%}
.photo{position:absolute;background:linear-gradient(160deg,#e9ece8 0%,#b9bfc2 45%,#6d7479 100%)}
.front .hero{left:18px;top:72px;width:540px;height:270px;border-radius:14px 14px 0 0}
.thumb{position:absolute;left:20px;width:132px;height:92px;border:4px solid var(--blue);border-radius:12px;background:linear-gradient(150deg,#d6dadc,#7f878b)}
.back .hero{left:20px;top:26px;width:536px;height:300px;border-radius:14px 14px 0 0;background:linear-gradient(170deg,#f1efe4 0%,#c9ccc8 50%,#8b9194 100%)}
.headline{position:absolute;left:0;top:20px;width:100%;text-align:center;font-family:"Roboto Condensed",Arial,sans-serif;font-weight:700;font-size:29px;color:var(--white);letter-spacing:.3px}
.point{position:absolute;text-transform:uppercase}
.point h2{font-weight:700;font-size:18.5px;line-height:22px;color:var(--blue)}
.point p{font-size:11px;line-height:14px;color:var(--ink);margin-top:2px}
.point strong{font-weight:700}
.offer{position:absolute;border-radius:50%;background:var(--navy);border:5px solid var(--sky);color:var(--white);text-align:center;display:flex;flex-direction:column;justify-content:center}
.offer.half{left:428px;top:516px;width:136px;height:136px}
.offer.half .big{font-size:32px;font-weight:900;line-height:36px}
.offer.half .big span{font-size:22px;font-weight:400}
.offer.half .small{font-size:20px;line-height:26px}
.offer.free{left:356px;top:300px;width:200px;height:200px;border-width:7px}
.offer.free .big{font-size:25px;font-weight:900;color:var(--lime);line-height:30px}
.offer.free .small{font-size:16px;font-weight:700;line-height:20px}
.contact{position:absolute;font-size:10px;line-height:13px;text-transform:uppercase}
.contact strong{font-weight:700}
.contact .web{text-transform:none}
.front .contact{left:28px;top:642px;color:var(--ink)}
.back .contact{right:10px;top:672px;text-align:right;color:var(--white)}
.hours{position:absolute;left:0;bottom:0;width:290px;height:30px;background:var(--navy);color:var(--white);font-weight:700;font-size:12px;line-height:30px;padding-left:16px}
.brand{position:absolute;display:flex;align-items:center;gap:10px}
.brand .dot{width:58px;height:58px;border-radius:50%;background:#eef2f6;border:3px solid #9aa6b3}
.brand .name{font-size:20px;line-height:24px;color:var(--white);font-weight:400;width:110px}
.front .brand{left:384px;top:680px}
.back .brand{left:18px;top:674px}
.back .band{position:absolute;left:0;top:664px;width:100%;height:83px;background:var(--navy);border-top:4px solid var(--lime)}
</style>
</head>
<body>
<div class="side-label front">FRONT</div>
<div class="side-label back">BACK</div>

<section class="page front">
  <svg class="shapes" viewBox="0 0 570 747" aria-hidden="true">
    <defs>
      <radialGradient id="bubbleFront" cx=".5" cy=".5" r=".5">
        <stop offset="0" stop-color="#ffffff"/>
        <stop offset="1" stop-color="#bfe2f7"/>
      </radialGradient>
    </defs>
    <rect width="570" height="747" fill="#2357b0"/>
    <rect x="8" y="72" width="554" height="640" fill="#ffffff"/>
    <circle cx="290" cy="470" r="140" fill="url(#bubbleFront)" opacity=".8"/>
    <circle cx="420" cy="600" r="110" fill="url(#bubbleFront)" opacity=".7"/>
    <circle cx="230" cy="640" r="80" fill="url(#bubbleFront)" opacity=".6"/>
  </svg>
  <h1 class="headline">FAST FORWARD YOUR LAUNDRY DAY</h1>
  <div class="photo hero" role="img" aria-label="Photo of the laundromat interior with rows of front-loading dryers"></div>
  <svg class="shapes" viewBox="0 0 570 747" aria-hidden="true">
    <path d="M8 330 C150 330 190 300 300 305 C420 310 500 290 562 200 L562 712 L8 712 Z" fill="#ffffff"/>
    <path d="M8 330 C150 330 190 300 300 305 C420 310 500 290 562 200" fill="none" stroke="#2357b0" stroke-width="10"/>
    <path d="M270 747 C350 690 450 650 570 620 L570 650 C470 675 390 710 330 747 Z" fill="#3f9fe0"/>
    <path d="M275 747 C340 705 400 680 440 665 C400 690 360 720 330 747 Z" fill="#a6d13a"/>
    <path d="M330 747 C400 705 480 675 570 655 L570 747 Z" fill="#1b3f8c"/>
  </svg>
  <div class="thumb" style="top:322px" role="img" aria-label="Photo of stacked dryers"></div>
  <div class="thumb" style="top:432px" role="img" aria-label="Photo of commercial washers"></div>
  <div class="thumb" style="top:537px" role="img" aria-label="Photo of the folding area"></div>

  <div class="point" style="left:179px;top:350px">
    <h2>Hate going laundry ?</h2>
    <p>Will fast forward your day with our large commercial<br>washers and dryers : you will be out of here with&nbsp; in no time</p>
  </div>
  <div class="point" style="left:179px;top:414px">
    <h2>Have large laundry loads ?</h2>
    <p>Bring them in your car : we have ample parking</p>
  </div>
  <div class="point" style="left:179px;top:465px">
    <h2>Get bored doing laundry ?</h2>
    <p>Not here ! we have free wi fi and flat screen TV<br>to keep you entertain</p>
  </div>
  <div class="point" style="left:179px;top:533px">
    <h2>Our location is a<br>multitasker dream :</h2>
    <p>Grocery shoping at nearby Greenway,<br>lunch at Wok Garden (or Sub Stop<br>or Crispy Coop) coffee at Bean Corner</p>
  </div>

  <div class="offer half">
    <div class="big">50%<span> OFF</span></div>
    <div class="small">ON YOUR<br>1ST WASH</div>
  </div>

  <div class="contact">
    Contact us today:<br>
    <strong>Harlow Laundromat</strong><br>
    2210 C Harlow Street, San Francisco CA 94115<br>
    Tel : 415 555 0182<br>
    <span class="web">www.harlowlaundromat.com</span>
  </div>

  <div class="brand"><span class="dot"></span><span class="name">harlow laundromat</span></div>
  <div class="hours">OPEN EVERY DAT FROM 6A.M TO 10 P.M</div>
</section>

<section class="page back">
  <svg class="shapes" viewBox="0 0 570 747" aria-hidden="true">
    <defs>
      <radialGradient id="bubbleBack" cx=".5" cy=".5" r=".5">
        <stop offset="0" stop-color="#ffffff"/>
        <stop offset="1" stop-color="#c4e4f7"/>
      </radialGradient>
    </defs>
    <rect width="570" height="747" fill="#2357b0"/>
    <rect x="8" y="10" width="554" height="660" fill="#ffffff"/>
    <circle cx="230" cy="560" r="150" fill="url(#bubbleBack)" opacity=".8"/>
    <circle cx="110" cy="460" r="90" fill="url(#bubbleBack)" opacity=".6"/>
    <circle cx="400" cy="590" r="100" fill="url(#bubbleBack)" opacity=".6"/>
  </svg>
  <div class="photo hero" role="img" aria-label="Photo of customers using washers and dryers in the laundromat"></div>
  <svg class="shapes" viewBox="0 0 570 747" aria-hidden="true">
    <path d="M8 220 C40 330 160 318 300 318 C420 318 480 300 562 290 L562 747 L8 747 Z" fill="#ffffff"/>
    <path d="M8 220 C40 330 160 318 300 318 C420 318 480 300 562 290" fill="none" stroke="#2357b0" stroke-width="12"/>
    <path d="M8 240 C50 320 140 325 220 326" fill="none" stroke="#3f9fe0" stroke-width="4"/>
  </svg>

  <div class="offer free">
    <div class="big">FREE WASH</div>
    <div class="small">ON LOAD OF<br>20LB WASH FREE<br>WITH<br>THIS COUPON</div>
    <div class="small" style="font-size:14px">COUPON VALID :</div>
  </div>

  <div class="point" style="left:24px;top:382px">
    <h2>No time for laundry ?</h2>
    <p style="font-size:12px;line-height:15px">Bring it to us and collect it washed.<br>folded and neatly packed after 24 hours .</p>
  </div>
  <div class="point" style="left:24px;top:467px">
    <h2>No time for grocery shopping ?</h2>
    <p style="font-size:12px;line-height:15px">Do you grocery shopping at nearby <strong>Greenway</strong><br>while your machines do your laundry</p>
  </div>
  <div class="point" style="left:24px;top:550px">
    <h2>Tired of washing your cloth in<br>a dirty laundromat ?</h2>
    <p style="font-size:12px;line-height:15px">We have the cleanest laundromat in the<br>bay area with efficient atendants</p>
  </div>

  <div class="band"></div>
  <div class="brand"><span class="dot"></span><span class="name">harlow laundromat</span></div>
  <div class="contact">
    Contact us today:<br>
    <strong>Harlow Laundromat</strong><br>
    2210 C Harlow Street, San Francisco CA 94115<br>
    Tel : 415 555 0182<br>
    <span class="web">www.harlowlaundromat.com</span>
  </div>
</section>
</body>
</html>
```